Covid19 Poster for workplaces

Create a poster on how to protect yourself from Corona virus at work.
We are a Staffwell Collective company. We have just re-branded so we need to fit in with our brand. We like clean and fresh, slightly amusing is ok if it will draw attention but it's an important topic. A4 and A3 please.

Content:

Headline: Lower the risk of COVID 19 in the workplace.

BE WELL

Bring your own cup - don’t share cups and food.
Elbow tap instead of handshakes and kisses
Wash your hands often - with soap.
Elbow or tissues when you cough or sneeze then straight in the bin
Leave your face alone after touching shared surfaces
Leave your bugs at home if you’re feeling unwell.

Call health line if you have a cough, a high temperature and shortness of breath. 0800 472 9160

Based on recommendations from ZPK and QLN

Target Market(s)

Employees - so anyone

Other font styles liked:
• Use the closest font to the brand documents

Requirements
Should not have
• Clip art

```html
<!DOCTYPE html>
<html lang="en">
<head>
<meta charset="utf-8">
<title>Wellbeing Matters at Work – Lower the risk of COVID 19</title>
<link rel="stylesheet" href="https://fonts.googleapis.com/css2?family=Archivo:wght@800&family=Figtree:wght@400;600;700&display=swap">
<style>
  :root {
    --teal: #1aacb5;
    --teal-text: #1ba8b4;
    --ink: #111111;
    --paper: #ffffff;
    --photo-dark: #2b3a4c;
    --photo-mid: #4a6a8a;
    --photo-warm: #c9a27a;
  }
  * { box-sizing: border-box; margin: 0; padding: 0; }
  html, body { width: 863px; height: 1200px; overflow: hidden; background: var(--paper); }
  .poster {
    position: relative;
    width: 863px;
    height: 1200px;
    background: var(--paper);
    font-family: "Figtree", Arial, sans-serif;
    color: var(--ink);
  }
  .hero-photo {
    position: absolute;
    left: 247px;
    top: 23px;
    width: 369px;
    height: 198px;
    border-radius: 99px;
    background: linear-gradient(120deg, var(--photo-warm) 0%, var(--photo-mid) 45%, var(--photo-dark) 100%);
  }
  .title {
    position: absolute;
    left: 0;
    width: 100%;
    top: 244px;
    text-align: center;
    font-family: "Archivo", Arial, sans-serif;
    font-weight: 800;
    font-size: 39px;
    letter-spacing: 2.6px;
    line-height: 1;
  }
  .subtitle {
    position: absolute;
    left: 0;
    width: 100%;
    top: 318px;
    text-align: center;
    color: var(--teal-text);
    font-weight: 700;
    font-size: 32px;
    letter-spacing: -0.3px;
    line-height: 1;
  }
  .tips { list-style: none; }
  .tip {
    position: absolute;
    left: 32px;
    font-size: 22.5px;
    line-height: 32px;
  }
  .tip svg {
    position: absolute;
    left: 0;
    top: -6px;
    width: 37px;
    height: 31px;
  }
  .tip span { display: block; margin-left: 49px; }
  .tip--call span { margin-left: 45px; }
  .brand-band {
    position: absolute;
    left: 0;
    top: 1000px;
    width: 100%;
    height: 200px;
    background: var(--teal);
  }
  .brand-name {
    position: absolute;
    left: 0;
    width: 100%;
    top: 48px;
    text-align: center;
    color: var(--paper);
    font-weight: 700;
    font-size: 46px;
    line-height: 1;
    letter-spacing: -0.5px;
  }
  .brand-name::before {
    content: "";
    display: inline-block;
    width: 34px;
    height: 34px;
    border-radius: 50%;
    background: var(--paper);
    margin-right: 16px;
    vertical-align: -2px;
  }
  .brand-url {
    position: absolute;
    left: 0;
    width: 100%;
    top: 157px;
    text-align: center;
    font-size: 23px;
    line-height: 1;
    color: var(--ink);
  }
</style>
</head>
<body>
<main class="poster">
  <div class="hero-photo" role="img" aria-label="Photo of smiling colleagues working together at office desks"></div>

  <h1 class="title">Wellbeing Matters at Work</h1>
  <h2 class="subtitle">Lower the risk of COVID 19 in the workplace</h2>

  <ul class="tips">
    <li class="tip" style="top:410px"><svg viewBox="0 0 37 31" aria-hidden="true"><path d="M1 17 L10 29 Q20 12 36 1 Q22 9 10 23 Z" fill="#111"/></svg><span>Bring your cup - don’t share cups and food</span></li>
    <li class="tip" style="top:482px"><svg viewBox="0 0 37 31" aria-hidden="true"><path d="M1 17 L10 29 Q20 12 36 1 Q22 9 10 23 Z" fill="#111"/></svg><span>Elbow tap instead of handshakes and kisses</span></li>
    <li class="tip" style="top:555px"><svg viewBox="0 0 37 31" aria-hidden="true" style="top:-16px"><path d="M1 17 L10 29 Q20 12 36 1 Q22 9 10 23 Z" fill="#111"/></svg><span>Wash your hands often - with soap</span></li>
    <li class="tip" style="top:628px"><svg viewBox="0 0 37 31" aria-hidden="true" style="top:-16px"><path d="M1 17 L10 29 Q20 12 36 1 Q22 9 10 23 Z" fill="#111"/></svg><span>Elbow or tissues when you cough or sneeze then straight in the bin</span></li>
    <li class="tip" style="top:701px"><svg viewBox="0 0 37 31" aria-hidden="true" style="top:-10px"><path d="M1 17 L10 29 Q20 12 36 1 Q22 9 10 23 Z" fill="#111"/></svg><span>Leave your face alone after touching shared surfaces</span></li>
    <li class="tip" style="top:773px"><svg viewBox="0 0 37 31" aria-hidden="true"><path d="M1 17 L10 29 Q20 12 36 1 Q22 9 10 23 Z" fill="#111"/></svg><span>Leave your bugs at home if you’re feeling unwell</span></li>
    <li class="tip tip--call" style="top:838px"><svg viewBox="0 0 37 31" aria-hidden="true" style="top:-8px"><path d="M1 17 L10 29 Q20 12 36 1 Q22 9 10 23 Z" fill="#111"/></svg><span>Call health line if you have a cough, high temperature or shortness<br>of breath at 0800 472 9160</span></li>
  </ul>

  <footer class="brand-band">
    <div class="brand-name">Staffwell Collective</div>
    <div class="brand-url">staffwellcollective.co.nz</div>
  </footer>
</main>
</body>
</html>
```